Young Accounting firm needing a captivating business card

We need a business card design that forces the person to look at the card because its either gold foil, plastic, or lettering pop up etc. We already have a logo with a specific gold color and we need to make it pop. We are an accounting firm. I need the words" accounting, payroll, licenses, audits, taxes" somewhere on the business card so as to describe what we do- preferably on the side where the logo is at.

Industry/Entity Type

Accounting

Contact Information for Business Card

Address 48276 9th Ave S Ste 305, Federal Way, WA 98117
Business Phone (360)418-2096
Fax (360)418-2157
Office Cell Phone (360)586-7319

Font styles to use
Serif

Colors
85abd2

Requirements
Must have
• It should state
• "Accounting" "Taxes" "Audits" "Licenses" "Payroll"
Nice to have
• Matte with gold foil, different textures, With Either a textured ivory background or gray blue slate background
Should not have
• colorful colors

```html
<!DOCTYPE html>
<html lang="en">
<head>
<meta charset="utf-8">
<title>Kelvora Ledger – Business Card</title>
<link href="https://fonts.googleapis.com/css2?family=Roboto:wght@400;500&family=Roboto+Condensed:wght@700&display=swap" rel="stylesheet">
<style>
  :root {
    --backdrop: #d9d9da;
    --card: #f4f4f2;
    --gold: #c6a04a;
    --gold-light: #e2c678;
    --gold-dark: #a8832f;
    --blue: #85abd2;
    --ink: #1c1c1c;
    --ink-soft: #3a3a3a;
  }
  * { margin: 0; padding: 0; box-sizing: border-box; }
  html, body { width: 1200px; height: 852px; overflow: hidden; }
  body {
    background: var(--backdrop);
    font-family: "Roboto", Arial, sans-serif;
    position: relative;
  }
  .card {
    position: absolute;
    width: 500px;
    height: 286px;
    background: var(--card);
    border-radius: 14px;
    box-shadow: 0 6px 18px rgba(0,0,0,0.18);
    overflow: hidden;
  }
  .card--front { left: 70px; top: 190px; }
  .card--back { left: 630px; top: 376px; }

  .brand {
    display: flex;
    align-items: center;
    gap: 10px;
    color: var(--gold);
    font-weight: 500;
    letter-spacing: 0.5px;
    white-space: nowrap;
  }
  .brand__mark { background: var(--gold); border-radius: 4px; flex: none; }

  .card--front .brand {
    position: absolute; left: 0; right: 0; top: 92px;
    justify-content: center; font-size: 40px;
  }
  .card--front .brand__mark { width: 34px; height: 34px; }
  .services {
    position: absolute; left: 0; right: 0; top: 190px;
    text-align: center; font-size: 13px; color: var(--ink-soft);
    letter-spacing: 0.4px;
  }
  .services .sep { color: var(--gold); margin: 0 7px; }

  .card__art { position: absolute; inset: 0; }
  .holder {
    position: absolute; right: 26px; top: 20px; text-align: right;
  }
  .holder__name {
    font-family: "Roboto Condensed", Arial, sans-serif;
    font-weight: 700; font-size: 20px; color: var(--ink);
  }
  .holder__title { font-size: 12px; color: var(--ink-soft); margin-top: 2px; }

  .card--back .brand {
    position: absolute; left: 28px; top: 150px; font-size: 28px;
  }
  .card--back .brand__mark { width: 24px; height: 24px; }

  .contacts {
    position: absolute; right: 22px; top: 134px;
    list-style: none; font-size: 12px; color: var(--ink);
    text-align: right; line-height: 19px;
  }
  .contacts li { display: flex; justify-content: flex-end; align-items: center; gap: 7px; }
  .contacts svg { width: 11px; height: 11px; fill: var(--gold); flex: none; }

  .address {
    position: absolute; left: 30px; bottom: 22px;
    font-size: 12.5px; color: var(--ink); line-height: 18px;
  }
</style>
</head>
<body>
  <section class="card card--front" aria-label="Business card front">
    <div class="brand"><span class="brand__mark"></span><span class="brand__name">Kelvora Ledger</span></div>
    <p class="services">Accounting<span class="sep">|</span>Taxes<span class="sep">|</span>Audits<span class="sep">|</span>Licenses<span class="sep">|</span>Payroll</p>
  </section>

  <section class="card card--back" aria-label="Business card back">
    <svg class="card__art" viewBox="0 0 500 286" aria-hidden="true">
      <defs>
        <linearGradient id="goldSweep" x1="0" y1="1" x2="1" y2="0">
          <stop offset="0" stop-color="#a8832f"/>
          <stop offset="0.55" stop-color="#c6a04a"/>
          <stop offset="1" stop-color="#e2c678"/>
        </linearGradient>
      </defs>
      <path class="swoosh-gold" d="M0 0 H500 V80 C420 96 340 110 250 104 C160 98 80 40 0 52 Z" fill="url(#goldSweep)"/>
      <path class="swoosh-blue" d="M0 100 C80 74 170 120 260 122 C360 124 430 104 500 94" fill="none" stroke="#85abd2" stroke-width="7"/>
    </svg>

    <div class="holder">
      <p class="holder__name">Marisol Ortega</p>
      <p class="holder__title">Founder / President</p>
    </div>

    <div class="brand"><span class="brand__mark"></span><span class="brand__name">Kelvora Ledger</span></div>

    <ul class="contacts">
      <li>(360)418-2096 <svg viewBox="0 0 12 12"><path d="M2 1h3l1 3-2 1a7 7 0 0 0 3 3l1-2 3 1v3a1 1 0 0 1-1 1A10 10 0 0 1 1 2a1 1 0 0 1 1-1z"/></svg></li>
      <li>(360)418-2157 <svg viewBox="0 0 12 12"><path d="M3 1h5v3H3zM1 5h10v5H1zM3 8h6v3H3z"/></svg></li>
      <li>(360)586-7319 <svg viewBox="0 0 12 12"><path d="M3 0h6a1 1 0 0 1 1 1v10a1 1 0 0 1-1 1H3a1 1 0 0 1-1-1V1a1 1 0 0 1 1-1zm0 2v7h6V2z"/></svg></li>
      <li>M.Ortega@KelvoraLedger.com <svg viewBox="0 0 12 12"><path d="M0 2h12v8H0zm1 1 5 4 5-4z"/></svg></li>
      <li>www.KelvoraLedger.com <svg viewBox="0 0 12 12"><circle cx="6" cy="6" r="5.5"/></svg></li>
    </ul>

    <p class="address">48276 9th Ave S Ste 305,<br>Federal Way, WA 98117</p>
  </section>
</body>
</html>
```